Website redesign for Maplecrest Drip Clinic

We need website redesign for Maplecrest Drip Clinic - Natural Health & Wellness Center.
In addition to our IV Infusions & Intramuscular Injection, our team offers a full spectrum of natural healing modalities to optimize physical, emotional and spiritual well being.
our current website is www.maplecrestdripcare.com
Our major competitor is https://brisknookhydra.com/
See uploaded design of current logo.
Target Market(s)
Health, fitness, functional medicine, immune boosting, alternative medicine, holistic medicine, supplements
Industry/Entity Type
Health And Wellness
Logo Text
Maplecrest Drip Clinic - Natural Health & Wellness Center
Number of Pages Required
5+ page
Requirements
Must have
- Contemporary Professional / Medical / Health Professional Look
Our current website is www.maplecrestdripcare.com

```html
<!DOCTYPE html>
<html lang="en">
<head>
<meta charset="utf-8">
<title>Maplecrest Drip Clinic — Natural Health &amp; Wellness</title>
<link href="https://fonts.googleapis.com/css2?family=Lato:wght@400;700&family=Quicksand:wght@300;400;500;600&display=swap" rel="stylesheet">
<style>
:root{
  --lime:#a3d12b;
  --lime-band:#a6d12f;
  --navy:#262f5e;
  --indigo:#2f2f86;
  --ink:#1f1f1f;
  --muted:#666;
  --footer:#2c2c2c;
  --footer-deep:#212121;
  --white:#fff;
}
*{box-sizing:border-box;margin:0;padding:0}
html,body{width:1200px;height:3685px;overflow:hidden;background:var(--white)}
body{position:relative;font-family:'Quicksand',sans-serif;color:var(--ink)}
.abs{position:absolute}
a{color:inherit;text-decoration:none}

/* header */
.site-header{left:0;top:0;width:1200px;height:79px;background:var(--white)}
.brand{left:89px;top:12px;display:flex;align-items:center;gap:10px}
.brand-dot{width:38px;height:38px;border-radius:50%;background:var(--navy)}
.brand-name{font-family:'Lato',sans-serif;font-weight:700;font-size:21px;color:var(--navy);line-height:1}
.brand-tag{font-family:'Lato',sans-serif;font-weight:700;font-size:13px;color:var(--navy);margin-top:3px}
.main-nav{left:405px;top:30px;display:flex;gap:25px;font-family:'Lato',sans-serif;font-size:16px;color:#222}
.main-nav .current{color:var(--lime)}
.cart{left:1094px;top:32px}

/* hero */
.hero{left:0;top:79px;width:1200px;height:532px;background:linear-gradient(120deg,#3b2f28 0%,#5a4a40 35%,#2c2a2b 60%,#4a3a30 100%)}
.hero-title{left:0;top:228px;width:1200px;text-align:center;font-family:'Lato',sans-serif;font-weight:700;font-size:67px;color:var(--white)}
.hero-sub{left:0;top:302px;width:1200px;text-align:center;font-weight:400;font-size:38px;color:var(--white)}
.btn-lime{left:489px;top:382px;width:222px;height:64px;border-radius:32px;background:var(--lime);color:var(--white);font-weight:500;font-size:23px;display:flex;align-items:center;justify-content:center}

/* care section */
.section-title{left:0;width:1200px;text-align:center;font-family:'Lato',sans-serif;font-weight:700;font-size:37px;color:var(--ink)}
.section-title .accent{color:var(--navy)}
.title-rule{left:576px;width:48px;height:4px;background:var(--lime)}
.care-item{top:791px;width:300px;text-align:center}
.care-item svg{display:block;margin:0 auto}
.care-item h3{font-family:'Lato',sans-serif;font-weight:400;font-size:18px;margin-top:22px;color:var(--ink)}
.care-item p{font-size:15px;line-height:25px;color:var(--muted);margin-top:10px;height:112px}
.care-item .strong{color:var(--navy);font-weight:500}
.care-item .link{font-size:15px;color:var(--lime)}

/* welcome band */
.welcome{left:0;top:1122px;width:1200px;height:658px;background:var(--lime-band)}
.welcome-title{left:606px;top:1272px;font-family:'Lato',sans-serif;font-weight:700;font-size:36px;line-height:45px;color:var(--white)}
.welcome-rule{left:606px;top:1385px;width:47px;height:4px;background:var(--white)}
.welcome-text{left:606px;top:1420px;width:520px;font-size:18px;line-height:29px;color:var(--white)}
.btn-navy{left:606px;top:1570px;width:172px;height:52px;border-radius:26px;background:var(--navy);color:var(--white);font-family:'Lato',sans-serif;font-size:18px;display:flex;align-items:center;justify-content:center}

/* menu cards */
.menu-card{width:243px;height:286px;background:var(--white);box-shadow:0 2px 10px rgba(0,0,0,.14);text-align:center;padding-top:18px}
.menu-card h3{font-family:'Lato',sans-serif;font-weight:700;font-size:31px;line-height:43px;color:var(--navy)}
.menu-card p{font-size:17px;line-height:29px;color:#555;margin-top:8px;padding:0 10px}
.menu-card .book{position:absolute;left:0;bottom:22px;width:100%;font-size:17px;color:var(--lime)}

/* packages */
.pack{top:2678px;width:400px;height:437px;text-align:center;color:var(--white);padding-top:98px}
.pack h3{font-family:'Lato',sans-serif;font-weight:400;font-size:37px}
.pack h4{font-family:'Lato',sans-serif;font-weight:700;font-size:20px;margin-top:6px}
.pack p{font-size:18px;line-height:29px;margin-top:18px;padding:0 50px}
.pack-a{left:0;background:var(--indigo)}
.pack-b{left:400px;background:var(--lime-band)}
.pack-c{left:800px;background:var(--indigo)}

/* footer */
.site-footer{left:0;top:3115px;width:1200px;height:570px;background:var(--footer)}
.newsletter{left:87px;top:3172px;width:1026px;height:134px;background:var(--footer-deep)}
.newsletter-label{left:133px;top:3226px;font-family:'Lato',sans-serif;font-weight:700;font-size:21px;color:var(--white)}
.newsletter-input{left:512px;top:3218px;width:505px;height:46px;background:var(--white);font-family:'Lato',sans-serif;font-size:13px;color:#555;padding:15px 0 0 33px}
.newsletter-send{left:1017px;top:3218px;width:47px;height:46px;background:var(--lime);display:flex;align-items:center;justify-content:center}
.foot-col{top:3343px;font-family:'Lato',sans-serif;color:var(--white)}
.foot-col h4{font-weight:700;font-size:18px;margin-bottom:22px}
.foot-col li{list-style:none;font-size:13.5px;line-height:31.4px}
.foot-col .contact li{line-height:24px}
.socials{display:flex;gap:26px;margin-top:8px}
.socials span{width:16px;height:16px;border-radius:3px;background:var(--white)}
.copyright{left:0;top:3640px;width:1200px;text-align:center;font-family:'Lato',sans-serif;font-size:13px;color:var(--white)}
</style>
</head>
<body>

<header class="abs site-header">
  <div class="abs brand">
    <span class="brand-dot"></span>
    <div>
      <div class="brand-name">Maplecrest Drip Clinic</div>
      <div class="brand-tag">Natural Health &amp; Wellness</div>
    </div>
  </div>
  <nav class="abs main-nav">
    <a class="current">Home</a><a>Services</a><a>Intake Forms</a><a>Products</a><a>Our Team</a><a>Book Online</a><a>Contact Us</a>
  </nav>
  <svg class="abs cart" width="14" height="14" viewBox="0 0 14 14"><path d="M0 1h3l2 8h7l2-6H4" fill="none" stroke="#a3d12b" stroke-width="1.6"/><circle cx="6" cy="12" r="1.3" fill="#a3d12b"/><circle cx="11" cy="12" r="1.3" fill="#a3d12b"/></svg>
</header>

<section class="abs hero" role="img" aria-label="Clinic lounge interior with recliner chairs, sofa and wooden table"></section>
<h1 class="abs hero-title">Maplecrest Drip Clinic</h1>
<p class="abs hero-sub">Natural Health &amp; Wellness</p>
<a class="abs btn-lime">Get Started</a>

<h2 class="abs section-title" style="top:705px">Taking care of <span class="accent">your health</span></h2>
<div class="abs title-rule" style="top:768px"></div>

<div class="abs care-item" style="left:79px">
  <svg width="60" height="74" viewBox="0 0 60 74" fill="none" stroke="#a3d12b" stroke-width="2.4"><rect x="6" y="6" width="46" height="62" rx="3"/><rect x="20" y="2" width="18" height="8" rx="2"/><path d="M14 24h10M14 34h30M14 42h30M14 50h24M14 58h18"/><path d="M34 20c2-4 8-3 6 2l-6 5-6-5c-2-5 4-6 6-2z"/></svg>
  <h3>Functional Health Report</h3>
  <p>A Functional Health Report<br>takes your lab data and analyzes it to<br>help you understand what's going on<br>inside your body</p>
  <a class="link">Learn More</a>
</div>
<div class="abs care-item" style="left:449px">
  <svg width="84" height="74" viewBox="0 0 84 74" fill="none" stroke="#a3d12b" stroke-width="2.4"><circle cx="44" cy="18" r="14"/><circle cx="34" cy="38" r="12"/><circle cx="54" cy="40" r="10"/><path d="M4 54h14l12 6h20c4 0 4 6 0 6H34M18 70h36l24-16c4-3 0-8-4-6L54 58"/></svg>
  <h3>Online Dispensary</h3>
  <p>Nutracuticals - Online Store<br><span class="strong">Pharmaceutical Grade Supplements</span></p>
  <a class="link">Shop Now</a>
</div>
<div class="abs care-item" style="left:818px">
  <svg width="60" height="74" viewBox="0 0 60 74" fill="none" stroke="#a3d12b" stroke-width="2.4"><path d="M18 4h24M22 4v24L6 62c-2 5 1 8 6 8h36c5 0 8-3 6-8L38 28V4"/><path d="M12 50h36"/><circle cx="24" cy="60" r="3"/><circle cx="36" cy="56" r="3"/></svg>
  <h3>Laboratory Services</h3>
  <p>We provide the industry's most<br>advanced diagnostic services and<br>solutions - so you can make better<br>healthcare decisions.</p>
  <a class="link">Learn More</a>
</div>

<section class="abs welcome" role="img" aria-label="Clinic storefront photo under a lime green tint"></section>
<svg class="abs" style="left:0;top:1122px" width="600" height="658" viewBox="0 1122 600 658">
  <path role="img" aria-label="Clinic lounge with leather sofa" d="M262 1217 C342 1300 462 1420 462 1537 A200 200 0 1 1 62 1537 C62 1420 182 1300 262 1217 Z" fill="#4a4240"/>
  <path role="img" aria-label="Nurse preparing a client for an IV infusion" d="M410 1184 C460 1260 566 1350 566 1430 A136 136 0 1 1 294 1430 C294 1350 360 1260 410 1184 Z" fill="#8a5a4e" stroke="#a6d12f" stroke-width="10"/>
</svg>
<h2 class="abs welcome-title">Welcome to Maplecrest Drip Clinic<br>Natural Health &amp; Wellness</h2>
<div class="abs welcome-rule"></div>
<div class="abs welcome-text">
  <p>Our team offers a full spectrum of healing modalities to optimize your physical, emotional and spiritual well being.</p>
  <p style="margin-top:30px">Check out our list of treatments and services below</p>
</div>
<a class="abs btn-navy">Book Now</a>

<h2 class="abs section-title" style="top:1876px">IV Infusion <span class="accent">Menu</span></h2>
<div class="abs title-rule" style="top:1945px"></div>

<div class="abs menu-card" style="left:90px;top:1982px"><h3>Inner Beauty<br>$150</h3><p>Reduce The Appearence<br>Of Wrinkles, Acne,<br>And Tired Skin</p><a class="book">Book Now</a></div>
<div class="abs menu-card" style="left:349px;top:1982px"><h3>Alleviate PMS<br>$150</h3><p>Reduce Bloating, Irritability, Abdominal Discomfort And More</p><a class="book">Book Now</a></div>
<div class="abs menu-card" style="left:608px;top:1982px"><h3>Vitality Cocktail<br>$175</h3><p>Reduces Seasonal Allergies, Fatigue And Inflammation, And Restore Natural Balance</p><a class="book">Book Now</a></div>
<div class="abs menu-card" style="left:867px;top:1982px"><h3>Immunity<br>$175</h3><p>Strengthen<br>Your Immune System<br>And Feel Better<br>Faster</p><a class="book">Book Now</a></div>

<div class="abs menu-card" style="left:90px;top:2289px"><h3>Quench<br>$175</h3><p>Hydrate And<br>Combat Fatigue<br>From Dehydration</p><a class="book">Book Now</a></div>
<div class="abs menu-card" style="left:349px;top:2289px"><h3>Get-Up-And-Go<br>$175</h3><p>Reduce The<br>Appearence<br>Of Wrinkles, Acne,<br>And Tired Skin</p><a class="book">Book Now</a></div>
<div class="abs menu-card" style="left:608px;top:2289px"><h3>Recovery &amp;<br>Performance<br>$175</h3><p style="margin-top:0">Decrease Recovery<br>Time And Enhance<br>Your Performance</p><a class="book">Book Now</a></div>
<div class="abs menu-card" style="left:867px;top:2289px"><h3>Boosters with<br>IV's $50</h3><p>Boosters Intramuscular Injection (IM) &nbsp;$50<br>Two or more Injections<br>$35 |</p><a class="book">Book Now</a></div>

<div class="abs pack pack-a" role="img" aria-label="Client receiving an infusion, tinted indigo"><h3>4 Pack ivs</h3><h4>4 Pack - $500 &nbsp;includes:</h4><p>Any four IV Infusions<br>Regular price $175 ea<br>Total Package Value &nbsp;&nbsp;&nbsp;$700 ($200 savings)<br>Your price &nbsp;$125 each</p></div>
<div class="abs pack pack-b" role="img" aria-label="Clients relaxing in infusion chairs, tinted lime"><h3>6 pack ivs</h3><h4>6 Pack - $660 &nbsp;includes:</h4><p>Any Six IV Infusions<br>Regular price $175 ea<br>Total Package Value &nbsp;&nbsp;&nbsp;$1050 ($390 savings)<br>Your price - $110 each</p></div>
<div class="abs pack pack-c" role="img" aria-label="Infusion room interior, tinted indigo"><h3>12 pack ivs</h3><h4>12 Pack - $1200 includes:</h4><p>Any twelve IV Infusions<br>Regular price $175 ea<br>Total Package Value &nbsp;&nbsp;&nbsp;$2100 ($900 savings)<br>Your price - $100 each</p></div>

<footer class="abs site-footer"></footer>
<div class="abs newsletter"></div>
<div class="abs newsletter-label">SIGN UP OUR NEWSLETTER</div>
<div class="abs newsletter-input">Email Address</div>
<div class="abs newsletter-send"><svg width="20" height="20" viewBox="0 0 20 20" fill="none" stroke="#fff" stroke-width="1.6"><path d="M2 9l16-7-6 16-3-7z M9 11l9-9"/></svg></div>

<div class="abs foot-col" style="left:87px"><h4>COMPANY</h4><ul><li>Home</li><li>Services</li><li>Intake Forms</li><li>Products</li><li>Our Team</li><li>Book Online</li><li>Contact Us</li></ul></div>
<div class="abs foot-col" style="left:365px"><h4>CONTACT</h4><ul class="contact" style="margin-top:31px"><li>555.014.2290</li><li>hello@maplecrestdripcare.com</li><li>1420 Birchwood Lane</li><li>Maplecrest, FL 30000</li></ul></div>
<div class="abs foot-col" style="left:704px"><h4>LEGAL</h4><ul><li>Privacy Policy</li><li>Faq</li><li>Sitemap</li><li>Contact Us</li></ul></div>
<div class="abs foot-col" style="left:977px"><h4>MY ACCOUNT</h4><ul><li>Log in</li><li>Sign Up</li></ul><h4 style="margin-top:28px;margin-bottom:14px">FOLLOW US</h4><div class="socials"><span></span><span></span><span></span></div></div>

<div class="abs copyright">© 2020 Maplecrest Drip Clinic</div>
</body>
</html>
```